Wheels for Elders Website Design

We need a NEW design and uploaded to Hostquill.com. Here is the current site: http://www.wheelsforelders.org

Need a form like this:

https://youthautogifts.org/

```html
<!DOCTYPE html>
<html lang="en">
<head>
<meta charset="utf-8">
<title>Wheels for Elders – Car Donation Charity</title>
<link rel="stylesheet" href="https://fonts.googleapis.com/css2?family=Montserrat:wght@400;600;700&family=Gochi+Hand&display=swap">
<style>
  :root {
    --sky: #a7c0d9;
    --wave-top: #b4c2e2;
    --wave-bottom: #e2edf1;
    --nav-active: #c0394f;
    --nav: #3f5b7a;
    --title: #6e3b66;
    --body-text: #4a5d78;
    --footer-text: #3d4f6e;
    --button: #272a5c;
    --button-text: #f5e96a;
    --frame: #f2e100;
    --white: #ffffff;
  }
  * { margin: 0; padding: 0; box-sizing: border-box; }
  html, body { width: 1200px; height: 675px; overflow: hidden; background: var(--white); }
  .page {
    position: relative;
    width: 1200px;
    height: 675px;
    overflow: hidden;
    font-family: "Montserrat", Arial, sans-serif;
    background: var(--white);
  }
  .backdrop { position: absolute; inset: 0; width: 1200px; height: 675px; }

  .main-nav {
    position: absolute;
    top: 26px;
    left: 710px;
    display: flex;
    gap: 48px;
    font-size: 20px;
    font-weight: 600;
  }
  .main-nav a { color: var(--nav); text-decoration: none; }
  .main-nav .is-active { color: var(--nav-active); }
  .main-nav .login { text-decoration: underline; text-underline-offset: 3px; text-decoration-thickness: 1.5px; }

  .hero-visual {
    position: absolute;
    left: 0;
    top: 114px;
    width: 512px;
    height: 442px;
    border-radius: 0 60px 40px 0;
    background:
      linear-gradient(180deg, #f4ef8a 0%, #f6f3a8 28%, #e77c78 45%, #e4676a 70%, #9b8d8f 85%, rgba(255,255,255,0) 100%);
  }

  .cta-frame {
    position: absolute;
    left: 354px;
    top: 424px;
    width: 162px;
    height: 55px;
    border: 1.5px solid var(--frame);
    transform: rotate(-3deg);
  }
  .cta-button {
    position: absolute;
    left: 373px;
    top: 433px;
    width: 117px;
    height: 33px;
    border-radius: 17px;
    background: var(--button);
    color: var(--button-text);
    font-family: "Gochi Hand", cursive;
    font-size: 16px;
    letter-spacing: 1px;
    display: flex;
    align-items: center;
    justify-content: center;
    transform: rotate(-3deg);
    text-decoration: none;
  }

  .hero-title {
    position: absolute;
    left: 690px;
    top: 192px;
    width: 440px;
    text-align: center;
    color: var(--title);
    font-weight: 700;
    font-size: 56px;
    line-height: 61px;
    letter-spacing: 0.5px;
  }
  .hero-text {
    position: absolute;
    left: 707px;
    top: 406px;
    width: 440px;
    color: var(--body-text);
    font-size: 15px;
    line-height: 18.7px;
  }
  .footer-text {
    position: absolute;
    left: 39px;
    top: 611px;
    width: 620px;
    color: var(--footer-text);
    font-size: 14.5px;
    line-height: 17px;
  }
</style>
</head>
<body>
<div class="page">
  <svg class="backdrop" viewBox="0 0 1200 675" aria-hidden="true">
    <defs>
      <linearGradient id="wave-fade" x1="0" y1="0" x2="0" y2="1">
        <stop offset="0" stop-color="var(--wave-top)"/>
        <stop offset="1" stop-color="var(--wave-bottom)"/>
      </linearGradient>
      <linearGradient id="ring-fade" x1="0" y1="0" x2="0" y2="1">
        <stop offset="0" stop-color="#a8c3dc"/>
        <stop offset="1" stop-color="#a8c3dc" stop-opacity="0.1"/>
      </linearGradient>
    </defs>
    <path class="sky-wave" fill="var(--sky)"
      d="M0 0 H935 C880 90 790 116 700 110 C560 100 420 30 250 33 C120 36 40 80 0 116 Z"/>
    <path class="ground-wave" fill="url(#wave-fade)"
      d="M387 675 C440 600 520 568 606 568 C740 568 830 612 932 615 C1050 618 1130 600 1200 578 V675 Z"/>
    <circle class="ring" cx="135" cy="666" r="74" fill="none" stroke="url(#ring-fade)" stroke-width="28"/>
  </svg>

  <nav class="main-nav">
    <a class="is-active" href="#">Home</a>
    <a href="#">About</a>
    <a href="#">Team</a>
    <a class="login" href="#">Log In</a>
  </nav>

  <div class="hero-visual" role="img" aria-label="Illustration of a colourful vintage camper van painted with flowers and a peace sign"></div>

  <svg style="position:absolute;left:49px;top:496px" width="24" height="22" viewBox="0 0 24 22" aria-hidden="true">
    <path d="M12 2 L22 20 H2 Z" fill="none" stroke="var(--white)" stroke-width="2.2" stroke-linejoin="round"/>
  </svg>

  <div class="cta-frame" aria-hidden="true"></div>
  <a class="cta-button" href="#">GET STARTED</a>

  <h1 class="hero-title">CAR DONATION<br>CHARITY</h1>
  <p class="hero-text">Lorem ipsum dolor sit amet, consectetur adipiscing elit, sed do eiusmod tempor incididunt ut labore et dolore magna aliqua. Quis ipsum suspendisse ultrices gravida.</p>

  <p class="footer-text">Lorem ipsum dolor sit amet, consectetur adipiscing elit, sed do eiusmod tempor incididunt ut labore et dolore magna aliqua. Quis ipsum suspendisse ultrices gravida.</p>

  <svg class="social-links" style="position:absolute;left:1018px;top:619px" width="170" height="32" viewBox="0 0 170 32" role="img" aria-label="Social media links">
    <circle cx="16" cy="15" r="12" fill="var(--white)" fill-opacity="0.75"/>
    <circle cx="56" cy="16" r="12" fill="var(--white)" fill-opacity="0.75"/>
    <circle cx="93" cy="16" r="12" fill="var(--white)" fill-opacity="0.75"/>
    <circle cx="133" cy="16" r="12" fill="var(--white)" fill-opacity="0.75"/>
  </svg>
</div>
</body>
</html>
```